Rent to Own Houses

We need an eye catching poster designed to interest good renters into entering rent to own agreements on houses. We should get them immediately interested buy explaining how they will benefit doing a rent own rather than just renting.

```html
<!DOCTYPE html>
<html lang="en">
<head>
<meta charset="utf-8">
<title>Rent to Own – Poster</title>
<link rel="stylesheet" href="https://fonts.googleapis.com/css2?family=Archivo:wdth,wght@62..125,100..900&family=Archivo+Black&display=swap">
<style>
  :root {
    --ink: #000000;
    --lime: #d6df1f;
    --canvas-w: 848px;
    --canvas-h: 1200px;
  }
  html, body {
    margin: 0;
    padding: 0;
    width: var(--canvas-w);
    height: var(--canvas-h);
    overflow: hidden;
    background: var(--lime);
  }
  .poster {
    position: relative;
    width: var(--canvas-w);
    height: var(--canvas-h);
    background: var(--lime);
    font-family: "Archivo", "Arial Black", sans-serif;
    font-weight: 800;
    font-stretch: 110%;
    overflow: hidden;
  }
  .poster__top {
    position: absolute;
    left: 0; top: 0;
    width: 100%;
    height: 569px;
    background: var(--ink);
  }
  .pain-points {
    position: absolute;
    left: 70px;
    top: 195px;
    margin: 0;
    color: var(--lime);
    font-size: 18px;
    line-height: 37px;
    letter-spacing: 0.3px;
  }
  .headline {
    position: absolute;
    left: 0; top: 0;
    width: var(--canvas-w);
    height: var(--canvas-h);
    margin: 0;
  }
  .headline__word {
    font-family: "Archivo Black", "Arial Black", sans-serif;
  }
  .pitch {
    position: absolute;
    right: 53px;
    top: 681px;
    margin: 0;
    text-align: right;
    color: var(--ink);
    font-size: 18px;
    line-height: 37px;
    letter-spacing: 0.3px;
  }
  .contact {
    position: absolute;
    right: 53px;
    top: 906px;
    margin: 0;
    text-align: right;
    color: var(--ink);
    font-size: 18px;
    line-height: 37px;
    letter-spacing: 0.3px;
    font-style: normal;
  }
  .contact__heading {
    display: block;
    text-transform: uppercase;
    margin-bottom: 5px;
  }
  .brand {
    position: absolute;
    right: 56px;
    top: 1090px;
    display: flex;
    flex-direction: column;
    align-items: flex-end;
    gap: 6px;
    color: var(--ink);
  }
  .brand__square {
    width: 40px;
    height: 40px;
    background: var(--ink);
  }
  .brand__name {
    font-size: 8px;
    line-height: 1;
    letter-spacing: 0.3px;
  }
</style>
</head>
<body>
<main class="poster">
  <div class="poster__top"></div>

  <p class="pain-points">
    Frustrated because you can't get a<br>
    mortgage for your dream house?<br>
    Nothing to show for your hard<br>
    earned money?<br>
    Are you tired of flushing your<br>
    money away renting?
  </p>

  <svg class="headline" viewBox="0 0 848 1200">
    <defs>
      <linearGradient id="house-key-tone" x1="0" y1="0" x2="0" y2="1">
        <stop offset="0" stop-color="#d6df1f"/>
        <stop offset="1" stop-color="#000000"/>
      </linearGradient>
    </defs>
    <text class="headline__word" x="69" y="567" font-size="60" fill="var(--lime)" letter-spacing="1">RENT TO</text>
    <rect class="headline__art" x="390" y="500" width="130" height="140" fill="url(#house-key-tone)"
          role="img" aria-label="Illustration of a house outline above a key whose ring forms the O of Own"/>
    <text class="headline__word" x="526" y="637" font-size="88" fill="var(--ink)">OWN</text>
  </svg>

  <p class="pitch">
    It does not matter the situation, if you<br>
    are a responsible person with a<br>
    steady income and you want to get<br>
    into a home of your own, we believe<br>
    we can help you.
  </p>

  <address class="contact">
    <span class="contact__heading">For more information contact</span>
    Prairie Key Homes<br>
    Contact number, company address<br>
    and website
  </address>

  <div class="brand">
    <span class="brand__square"></span>
    <span class="brand__name">PRAIRIE KEY HOMES</span>
  </div>
</main>
</body>
</html>
```